Car Detailing Brochure/PriceList

Looking for a nicely designed Brochure/Price sheet that can be displayed on the website and Chatterlane sites which details the different service stages available to potential customers

Target Market(s)

People in the local area who need paint enhancement and correction

Industry/Entity Type

Car Detailing

Requirements
Must have
• Reader Friendly, Informative, pictures (lots on Chatterlane/Website that can be used) would like to see nicely imbedded pictures relating to stages etc
Nice to have
• Luxury design following company branding with logo/colours etc https://www.thecorvalestudio.uk/services

```html
<!DOCTYPE html>
<html lang="en">
<head>
<meta charset="utf-8">
<title>The Corvale Studio – Detailing and Paint Correction Price List</title>
<link rel="stylesheet" href="https://fonts.googleapis.com/css2?family=Bebas+Neue&family=Oswald:wght@500;600;700&family=Arimo:wght@400&display=swap">
<style>
  :root {
    --orange: #f85a07;
    --orange-deep: #a8400a;
    --copper: #e0700f;
    --ink: #141414;
    --band: #222222;
    --paper: #ffffff;
    --mist: #e9e9ea;
    --chev: #9a9a9a;
    --rule: #8a8a8a;
  }
  * { margin: 0; padding: 0; box-sizing: border-box; }
  html, body { width: 1200px; height: 910px; overflow: hidden; background: var(--paper); }
  body { position: relative; font-family: "Arimo", Arial, sans-serif; color: var(--ink); }

  .sheet { position: absolute; left: 0; top: 55px; width: 1200px; height: 800px; overflow: hidden; }

  /* Header */
  .masthead { position: absolute; left: 0; top: 0; width: 1200px; height: 214px; }
  .masthead-bg {
    position: absolute; inset: 0;
    background:
      radial-gradient(ellipse 45% 80% at 50% 40%, #ffa640 0%, rgba(255,140,40,0.6) 35%, rgba(0,0,0,0) 75%),
      linear-gradient(90deg, #6b2a08 0%, #b4500e 22%, var(--copper) 50%, #b4500e 78%, #6b2a08 100%);
  }
  .brand { position: absolute; left: 128px; top: 48px; width: 600px; }
  .brand-name {
    font-family: "Bebas Neue", "Oswald", sans-serif; font-size: 84px; line-height: 80px;
    color: var(--ink); letter-spacing: 1px; white-space: nowrap;
  }
  .brand-tagline {
    font-family: "Bebas Neue", "Oswald", sans-serif; font-size: 52px; line-height: 50px;
    color: var(--paper); letter-spacing: 1.5px; margin-top: 16px; white-space: nowrap;
  }
  .contact {
    position: absolute; left: 875px; top: 29px; width: 298px; height: 164px;
    background: rgba(240,120,30,0.75); padding: 18px 0 0 30px; color: var(--paper);
    font-size: 18px; line-height: 23px;
  }
  .contact-line { display: flex; align-items: center; gap: 6px; white-space: nowrap; }
  .contact-line svg { width: 13px; height: 13px; flex: none; }
  .contact-rule { width: 83px; height: 3px; background: var(--paper); margin: 10px 0 12px; }

  /* Stages */
  .stages { position: absolute; left: 0; top: 214px; width: 1200px; height: 419px; }
  .stages-bg {
    position: absolute; inset: 0;
    background: linear-gradient(180deg, #ededee 0%, #e4e4e6 50%, #dcdde0 100%);
  }
  .stage { position: absolute; top: 8px; width: 300px; }
  .stage--one { left: 45px; }
  .stage--two { left: 388px; width: 316px; }
  .stage--three { left: 747px; width: 412px; }
  .stage-tag {
    display: inline-block; width: 145px; height: 68px; background: var(--orange);
    color: var(--paper); font-family: "Bebas Neue", sans-serif; font-size: 44px;
    line-height: 72px; padding-left: 14px; letter-spacing: 0.5px;
  }
  .stage-chevron { position: absolute; top: 22px; width: 44px; height: 34px; }
  .stage--one .stage-chevron { left: 228px; }
  .stage--two .stage-chevron { left: 230px; }
  .stage-copy {
    margin-top: 6px; font-size: 16.6px; line-height: 20.2px; text-align: justify;
    color: #1b1b1b; height: 250px;
  }
  .stage-copy strong {
    font-family: "Oswald", sans-serif; font-weight: 600; font-size: 14.4px;
    text-transform: uppercase; letter-spacing: -0.2px;
  }
  .price-table { position: relative; margin-top: 20px; }
  .price-table::before, .price-table::after {
    content: ""; position: absolute; left: -3px; width: 119px; height: 2px; background: var(--orange);
  }
  .price-table::before { top: -5px; }
  .price-table::after { top: 48px; }
  .price-row { display: flex; align-items: flex-end; }
  .price-cell { padding: 0 10px; border-left: 1.5px solid var(--ink); }
  .price-cell:first-child { padding-left: 0; border-left: none; }
  .price-label {
    font-family: "Oswald", sans-serif; font-weight: 600; font-size: 8px; line-height: 10px;
    text-transform: uppercase; white-space: nowrap; letter-spacing: -0.2px;
  }
  .price-value {
    font-family: "Oswald", sans-serif; font-weight: 600; font-size: 25px; line-height: 28px;
    letter-spacing: -0.5px;
  }
  .price-note {
    margin-top: 10px; font-family: "Oswald", sans-serif; font-weight: 600; font-size: 5px;
    text-transform: uppercase; white-space: nowrap;
  }

  /* Upgrades band */
  .upgrades { position: absolute; left: 0; top: 633px; width: 1200px; height: 167px; background: var(--band); }
  .upgrades-flag { position: absolute; left: 41px; top: -12px; width: 271px; height: 179px; }
  .upgrades-title {
    position: absolute; left: 73px; top: 14px; color: var(--paper);
    font-family: "Bebas Neue", sans-serif; font-size: 42px; line-height: 36px; letter-spacing: 0.3px;
  }
  .offer-row { position: absolute; right: 18px; display: flex; align-items: center; color: var(--paper); }
  .offer-row--top { top: 18px; }
  .offer-row--bottom { top: 95px; }
  .offer-row--top::after {
    content: ""; position: absolute; left: 4px; right: 290px; bottom: -6px; height: 1px; background: #555;
  }
  .offer { display: flex; align-items: center; }
  .offer-label { font-size: 13.5px; line-height: 17px; text-align: right; padding-right: 5px; border-right: 1px solid #777; }
  .offer-term {
    font-family: "Bebas Neue", sans-serif; font-size: 27px; line-height: 22px; padding-left: 4px;
    letter-spacing: -0.3px; white-space: nowrap;
  }
  .offer-from-rotated {
    font-family: "Bebas Neue", sans-serif; font-size: 27px; line-height: 22px; margin-left: 5px;
    writing-mode: vertical-rl; transform: rotate(180deg);
  }
  .offer-price {
    font-family: "Bebas Neue", sans-serif; font-size: 66px; line-height: 54px; padding-top: 4px;
    letter-spacing: -0.5px;
  }
  .offer-slash { width: 14px; height: 54px; margin: 0 12px 0 6px; flex: none; }
</style>
</head>
<body>
<main class="sheet">

  <header class="masthead">
    <div class="masthead-bg" role="img" aria-label="Brushed copper metal texture"></div>
    <div class="brand">
      <div class="brand-name">The Corvale Studio</div>
      <div class="brand-tagline">Detailing and Paint Correction</div>
    </div>
    <aside class="contact">
      <div class="contact-line">
        <svg viewBox="0 0 16 16" aria-hidden="true"><path fill="#fff" d="M3.6 1 6 3.4 4.6 5.4c.9 2 2.4 3.6 4.4 4.6l2-1.4L15 11l-1.3 3.2C8 14.5 1.5 8 1.8 2.3z"/></svg>
        <span>07700 900 418</span>
      </div>
      <div class="contact-line">
        <svg viewBox="0 0 16 16" aria-hidden="true"><rect x="1" y="3" width="14" height="10" fill="#fff"/><path d="M1 3l7 6 7-6" fill="none" stroke="#e0700f" stroke-width="1.3"/></svg>
        <span>hello@thecorvalestudio.uk</span>
      </div>
      <div class="contact-line">
        <svg viewBox="0 0 16 16" aria-hidden="true"><circle cx="8" cy="8" r="6.5" fill="none" stroke="#fff" stroke-width="1.4"/><path d="M1.5 8h13M8 1.5c-3 3.5-3 9.5 0 13M8 1.5c3 3.5 3 9.5 0 13" fill="none" stroke="#fff" stroke-width="1.2"/></svg>
        <span>www.thecorvalestudio.uk</span>
      </div>
      <div class="contact-rule"></div>
      <div>Opening Hours</div>
      <div>Mon - Sun: 7am - 10pm</div>
    </aside>
  </header>

  <section class="stages">
    <div class="stages-bg" role="img" aria-label="Faded photograph of a car front grille"></div>

    <article class="stage stage--one">
      <div class="stage-tag">Stage 1</div>
      <svg class="stage-chevron" viewBox="0 0 44 34" aria-hidden="true"><path d="M2 3l13 14L2 31M21 3l13 14-13 14" fill="none" stroke="var(--chev)" stroke-width="7"/></svg>
      <p class="stage-copy">Ideally suited to Brand new or exceptionally well-maintained vehicles. This Stage will remove light swirl marks, marring and micro scratches typically found in new car preparation or from home car washing methods. It includes; full inspection and prewash, wheels cleaned, snow foam, decontamination process, single stage machine polish, glass cleaned and a Liquid wax finish. <strong>This will give up to 6 months protection and takes between 1 - 1.5 days.</strong></p>
      <div class="price-table">
        <div class="price-row">
          <div class="price-cell"><div class="price-label">Small car</div><div class="price-value">£240</div></div>
          <div class="price-cell"><div class="price-label">Medium car</div><div class="price-value">£270</div></div>
          <div class="price-cell"><div class="price-label">Large car</div><div class="price-value">£300</div></div>
          <div class="price-cell"><div class="price-label">4x4/pickups/vans from</div><div class="price-value">£350</div></div>
        </div>
        <div class="price-note">*Upgrade to a hard wax finish with up to 12 months protection • Interior valet from £130</div>
      </div>
    </article>

    <article class="stage stage--two">
      <div class="stage-tag">Stage 2</div>
      <svg class="stage-chevron" viewBox="0 0 44 34" aria-hidden="true" style="left:458px;left:230px"><path d="M2 3l13 14L2 31M21 3l13 14-13 14" fill="none" stroke="var(--chev)" stroke-width="7"/></svg>
      <p class="stage-copy">This is our most popular package and will suit most vehicles. It includes everything from stage 1 plus a 2-stage polish that will address light scratches and imperfection, oxidation and begin to correct and level the paint surface resulting in an exceptional shine. Combined with a hard wax coating this will not only lock in the shine for longer but also make home cleaning and maintenance easier and more effective. <strong>This will give 6 -9 months protection and takes from 2.5 days</strong></p>
      <div class="price-table">
        <div class="price-row">
          <div class="price-cell"><div class="price-label">Small car</div><div class="price-value">£400</div></div>
          <div class="price-cell"><div class="price-label">Medium car</div><div class="price-value">£430</div></div>
          <div class="price-cell"><div class="price-label">Large car</div><div class="price-value">£460</div></div>
          <div class="price-cell"><div class="price-label">4x4/pickups/vans from</div><div class="price-value">£500</div></div>
        </div>
        <div class="price-note">*Upgrade to a ceramic coating with 2 - 3 years protection • Interior valet from £250</div>
      </div>
    </article>

    <article class="stage stage--three">
      <div class="stage-tag">Stage 3</div>
      <p class="stage-copy">This is our luxury level paint correction. It includes everything from stage 2 plus a 3 stage polish that will provide a glorious, better than new, mirror like shine. The 3 stage polish will remove medium to heavy scratches and will level the paint to give that wet look glossy finish you never thought possible. For the ultimate protection we recommend taking advantage of a professional grade ceramic coating which when applied will lock in that glossy finish and provide the longest possible protection. <strong>A full valet is included on this stage and with basic hard wax your protection will last up to 12 months and takes from 3.5 days.</strong></p>
      <div class="price-table">
        <div class="price-row">
          <div class="price-cell"><div class="price-label">Small car</div><div class="price-value">£600</div></div>
          <div class="price-cell"><div class="price-label">Medium car</div><div class="price-value">£630</div></div>
          <div class="price-cell"><div class="price-label">Large car</div><div class="price-value">£660</div></div>
          <div class="price-cell"><div class="price-label">4x4/pickups/vans from</div><div class="price-value">£700</div></div>
        </div>
        <div class="price-note">*Upgrade to a ceramic coating with 2 - 3 years protection • Interior valet from £250</div>
      </div>
    </article>
  </section>

  <section class="upgrades">
    <svg class="upgrades-flag" viewBox="0 0 271 179" aria-hidden="true"><path d="M0 0H230V68L259 97 230 126V179H0z" fill="var(--orange)"/></svg>
    <h2 class="upgrades-title">Upgrades<br>available on<br>all stages</h2>

    <div class="offer-row offer-row--top">
      <div class="offer">
        <div class="offer-label">Hard<br>Carnauba Wax<br>Protection</div>
        <div class="offer-term">1 Year<br>From</div>
        <div class="offer-price">£70</div>
        <svg class="offer-slash" viewBox="0 0 14 54" aria-hidden="true"><path d="M11 4 3 50" stroke="var(--orange)" stroke-width="4"/></svg>
      </div>
      <div class="offer">
        <div class="offer-label">Ceramic<br>paint<br>protection</div>
        <div class="offer-term">2-3 Year<br>From</div>
        <div class="offer-price">£200</div>
        <svg class="offer-slash" viewBox="0 0 14 54" aria-hidden="true"><path d="M11 4 3 50" stroke="var(--orange)" stroke-width="4"/></svg>
      </div>
      <div class="offer">
        <div class="offer-label">Ceramic<br>Wheel<br>Protection</div>
        <div class="offer-term">2-3 Year<br>From</div>
        <div class="offer-price">£100</div>
      </div>
    </div>

    <div class="offer-row offer-row--bottom">
      <div class="offer">
        <div class="offer-label">Interior valet; Full deep steam clean<br>including Carpets, Mats, leather<br>cleaner, Plastics and sanitisation</div>
        <div class="offer-from-rotated">From</div>
        <div class="offer-price">£80</div>
        <svg class="offer-slash" viewBox="0 0 14 54" aria-hidden="true"><path d="M11 4 3 50" stroke="var(--orange)" stroke-width="4"/></svg>
      </div>
      <div class="offer">
        <div class="offer-label">Ceramic<br>Leather<br>Protection</div>
        <div class="offer-term">2-3 Year<br>From</div>
        <div class="offer-price">£100</div>
        <svg class="offer-slash" viewBox="0 0 14 54" aria-hidden="true"><path d="M11 4 3 50" stroke="var(--orange)" stroke-width="4"/></svg>
      </div>
      <div class="offer">
        <div class="offer-label">Ceramic<br>Glass<br>Protection</div>
        <div class="offer-term">2-3 Year<br>From</div>
        <div class="offer-price">£40</div>
      </div>
    </div>
  </section>

</main>
</body>
</html>
```